Local Horticulturalist needs Business card design

Meridel Horticulture would like to update our existing business card and utilize our new logo (design attached)....we specialize in getting the best out of our customers yard with professional maintenance programs, expert pruning and hedging and garden restorations.
Utilizing colors from attached logo I would like a design that implies professionalism and if possible our businesses love of restoration through plants.
I also sometimes write down for my customers a start date and price on the back of my current card
Target Market(s)
Home owners
Contractors
Industry/Entity Type
Gardener
Contact Information for Business Card
Gareth Volkstrom | Horticulturalist
ph: 0438275946
meridelhort@fernmail.example
www.meridelhorticulture.example.au
Requirements
Must have
- crucial information easy to read
- incorporate current logo
- Horticulturalist listed preferably near name
Nice to have
- currently I write a job start date and price on the back of my current card so something that integrates this would be beneficial
Should not have
- be pretty or flowerey
- be too white or basic

```html
<!DOCTYPE html>
<html lang="en">
<head>
<meta charset="utf-8">
<title>Meridel Horticulture – Business Card</title>
<link rel="stylesheet" href="https://fonts.googleapis.com/css2?family=Open+Sans:wght@400;600;700&display=swap">
<style>
  :root {
    --bg: #2b2e33;
    --leaf: #85b942;
    --bark: #7a6a52;
    --paper: #f4f4f3;
    --ink: #2a2a2a;
    --rule: #c9c9c6;
    --white: #ffffff;
  }
  * { margin: 0; padding: 0; box-sizing: border-box; }
  html, body { width: 1200px; height: 864px; overflow: hidden; }
  body {
    background: var(--bg);
    font-family: "Open Sans", Arial, sans-serif;
    position: relative;
  }
  .card {
    position: absolute;
    width: 590px;
    height: 330px;
    border-radius: 3px;
  }
  /* Back of card */
  .card--back {
    left: 200px; top: 70px;
    background: var(--leaf);
    color: var(--white);
  }
  .card--back .brand {
    position: absolute; left: 130px; top: 98px;
  }
  .brand { display: flex; align-items: center; gap: 10px; }
  .brand__dot {
    width: 38px; height: 38px; border-radius: 50%;
    flex: none;
  }
  .card--back .brand__dot { background: var(--white); opacity: .85; }
  .brand__name { font-size: 24px; font-weight: 700; line-height: 1; }
  .brand__tagline { font-size: 12px; font-weight: 600; margin-top: 4px; letter-spacing: .2px; }
  .job-fields {
    position: absolute; left: 110px; top: 200px; right: 110px;
    display: flex; justify-content: space-between;
    font-size: 14px;
  }
  .job-field__line {
    display: inline-block; width: 88px;
    border-bottom: 1px solid var(--white); margin-left: 2px;
  }
  /* Front of card */
  .card--front {
    left: 420px; top: 470px;
    background: var(--paper);
    color: var(--ink);
  }
  .card--front .brand { position: absolute; right: 40px; top: 34px; }
  .card--front .brand__dot { background: var(--leaf); }
  .card--front .brand__name { color: var(--bark); }
  .card--front .brand__tagline { color: var(--bark); }
  .person { position: absolute; left: 60px; top: 96px; }
  .person__name { font-size: 23px; font-weight: 600; color: var(--leaf); line-height: 1.1; }
  .person__title { font-size: 13px; color: var(--ink); }
  .divider {
    position: absolute; left: 190px; right: 50px; top: 150px;
    border-top: 1px solid var(--rule);
  }
  .contact {
    position: absolute; right: 50px; top: 200px;
    list-style: none; text-align: right;
  }
  .contact__item {
    display: flex; justify-content: flex-end; align-items: center;
    gap: 10px; font-size: 15px; line-height: 26px;
  }
  .contact__icon {
    width: 16px; height: 16px; background: var(--leaf);
    border-radius: 2px; display: flex; align-items: center; justify-content: center;
  }
</style>
</head>
<body>
  <section class="card card--back" aria-label="Back of business card">
    <div class="brand">
      <span class="brand__dot"></span>
      <div>
        <div class="brand__name">Meridel Horticulture</div>
        <div class="brand__tagline">Garden Restorations &amp; Maintenance</div>
      </div>
    </div>
    <div class="job-fields">
      <span class="job-field">Start Date:<span class="job-field__line"></span></span>
      <span class="job-field">Price:<span class="job-field__line"></span></span>
    </div>
  </section>

  <section class="card card--front" aria-label="Front of business card">
    <div class="brand">
      <span class="brand__dot"></span>
      <div>
        <div class="brand__name">Meridel Horticulture</div>
        <div class="brand__tagline">Garden Restorations &amp; Maintenance</div>
      </div>
    </div>
    <div class="person">
      <div class="person__name">Gareth Volkstrom</div>
      <div class="person__title">Horticulturalist</div>
    </div>
    <div class="divider"></div>
    <ul class="contact">
      <li class="contact__item">0438275946
        <span class="contact__icon"><svg width="10" height="10" viewBox="0 0 10 10"><path d="M2 1h2l1 2-1 1c.5 1 1 1.5 2 2l1-1 2 1v2c-4 0-7-3-7-7z" fill="#fff"/></svg></span>
      </li>
      <li class="contact__item">meridelhort@fernmail.example
        <span class="contact__icon"><svg width="10" height="8" viewBox="0 0 10 8"><rect x=".5" y=".5" width="9" height="7" fill="none" stroke="#fff"/><path d="M.5 .5 5 4.5 9.5 .5" fill="none" stroke="#fff"/></svg></span>
      </li>
      <li class="contact__item">www.meridelhorticulture.example.au
        <span class="contact__icon"><svg width="10" height="10" viewBox="0 0 10 10"><path d="M4 6 6 4M3 5 1.5 6.5a1.4 1.4 0 0 0 2 2L5 7M7 5l1.5-1.5a1.4 1.4 0 0 0-2-2L5 3" fill="none" stroke="#fff" stroke-width="1.2"/></svg></span>
      </li>
    </ul>
  </section>
</body>
</html>
```